Bright Oak Fitness Facility Business Cards

Business Card Design that incorporates the logo and tagline

Target Market(s)

Fitness, People Who Exercise

Contact Information for Business Card

2817 Mossgrove Bend Road
Lakeview, Ohio 43190
Phone: 614-555-Jump (5867)
www.brightoakfitness.example
info@brightoakfitness.example

Requirements
Must have
• Logo, Address, Website, email and tagline "Beyond The Workout". Colors should be red/black/grey/white

```html
<!DOCTYPE html>
<html lang="en">
<head>
<meta charset="utf-8">
<title>Bright Oak Fitness – Business Cards</title>
<link href="https://fonts.googleapis.com/css2?family=Roboto:wght@400;500&family=Montserrat:wght@600&display=swap" rel="stylesheet">
<style>
  :root{
    --bg:#1a1a1a;
    --card-dark:#202020;
    --card-light:#f3f3f3;
    --red:#e0252f;
    --white:#ffffff;
    --ink:#1d1d1d;
    --silver:#9a9a9a;
  }
  html,body{margin:0;padding:0;overflow:hidden;}
  body{width:1200px;height:986px;background:var(--bg);position:relative;font-family:"Roboto",Arial,sans-serif;}
  .card{position:absolute;left:342px;width:516px;height:296px;border-radius:32px;overflow:hidden;}
  .card--front{top:160px;background:var(--card-light);}
  .card--back{top:530px;background:var(--card-dark);}
  .front-wave{position:absolute;inset:0;width:516px;height:296px;}
  .brand{position:absolute;font-family:"Montserrat",Arial,sans-serif;font-weight:600;white-space:nowrap;}
  .brand--front{right:48px;top:96px;font-size:22px;color:var(--ink);display:flex;align-items:center;gap:8px;}
  .brand-dot{width:12px;height:12px;border-radius:50%;background:var(--red);display:inline-block;}
  .person-name{position:absolute;left:37px;top:157px;margin:0;font-size:25px;font-weight:500;color:var(--red);}
  .person-role{position:absolute;left:37px;top:186px;margin:0;font-size:16px;color:var(--white);}
  .contact-list{position:absolute;left:37px;top:218px;margin:0;padding:0;list-style:none;color:var(--white);font-size:12.5px;line-height:17.6px;}
  .contact-list li{display:flex;align-items:center;gap:7px;}
  .contact-list svg{width:11px;height:11px;flex:none;}
  .address{position:absolute;right:50px;top:236px;margin:0;text-align:right;color:var(--white);font-size:12.5px;line-height:17.6px;font-style:normal;}
  .brand--back{left:0;right:0;top:154px;text-align:center;font-size:28px;color:var(--silver);}
  .tagline{position:absolute;left:0;right:0;top:250px;display:flex;justify-content:center;align-items:center;gap:9px;color:var(--white);font-size:11.5px;letter-spacing:.2px;}
  .tagline-rule{width:95px;height:2px;}
  .tagline-rule--left{background:linear-gradient(to right,transparent,var(--red) 55%);}
  .tagline-rule--right{background:linear-gradient(to left,transparent,var(--red) 55%);}
</style>
</head>
<body>
  <section class="card card--front">
    <svg class="front-wave" viewBox="0 0 516 296" aria-hidden="true">
      <path d="M0 64 C120 70 200 130 270 170 C340 205 420 205 516 196 L516 296 L0 296 Z" fill="var(--card-dark)"/>
      <path d="M52 70 C150 86 210 130 270 160 C340 192 420 190 516 178 L516 192 C420 202 340 202 268 168 C205 136 150 94 52 70 Z" fill="var(--red)"/>
    </svg>
    <div class="brand brand--front"><span class="brand-dot"></span>Bright Oak Fitness</div>
    <h1 class="person-name">Marcus T. Reed</h1>
    <p class="person-role">Director</p>
    <ul class="contact-list">
      <li><svg viewBox="0 0 12 12"><path d="M2.5 1 L4.5 1 L5.3 3.4 L4 4.4 C4.6 5.8 6 7.2 7.6 8 L8.6 6.7 L11 7.5 L11 9.5 C11 10.3 10.3 11 9.5 11 C5 11 1 7 1 2.5 C1 1.7 1.7 1 2.5 1 Z" fill="var(--red)"/></svg>614-555-Jump (5867)</li>
      <li><svg viewBox="0 0 12 12"><rect x="0.5" y="2" width="11" height="8" rx="1" fill="var(--red)"/><path d="M1 2.6 L6 6.6 L11 2.6" stroke="var(--card-dark)" stroke-width="1" fill="none"/></svg>info@brightoakfitness.example</li>
      <li><svg viewBox="0 0 12 12" fill="none" stroke="var(--red)" stroke-width="1"><circle cx="6" cy="6" r="5"/><ellipse cx="6" cy="6" rx="2.2" ry="5"/><path d="M1 6 H11 M2 3.3 H10 M2 8.7 H10"/></svg>www.brightoakfitness.example</li>
    </ul>
    <address class="address">2817 Mossgrove Bend Road<br>Lakeview, Ohio 43190</address>
  </section>

  <section class="card card--back">
    <div class="brand brand--back">Bright Oak Fitness</div>
    <div class="tagline"><span class="tagline-rule tagline-rule--left"></span>BEYOND THE WORKOUT<span class="tagline-rule tagline-rule--right"></span></div>
  </section>
</body>
</html>
```